" SOU MÉDICO ORTOPEDISTA COM ESPECIALIZAÇÃO EM CIRURGIA DO JOELHO E DO QUADRIL. REALIZO ATENDIMENTOS AMBULATORIAIS E CIRURGICOS NESTAS ARÉAS PRINCIPALMENTE. "

```html
<!DOCTYPE html>
<html lang="pt-BR">
<head>
<meta charset="UTF-8">
<title>Marcos Vieira de Andrade — Cartões</title>
<link href="https://fonts.googleapis.com/css2?family=Raleway:wght@300;400&display=swap" rel="stylesheet">
<style>
  :root {
    --backdrop: #e9e6e1;
    --navy-deep: #0c2440;
    --navy-mid: #163e63;
    --navy-light: #1d5282;
    --paper: #ffffff;
    --ink-light: #dfe7ef;
    --ink-muted: #9fb3c6;
    --ink-grey: #8b97a3;
    --ink-sub: #7e9cb8;
    --band-start: #1d4f86;
    --band-end: #3f9de0;
  }
  * { margin: 0; padding: 0; box-sizing: border-box; }
  html, body {
    width: 1200px; height: 1200px; overflow: hidden;
    background: var(--backdrop);
    font-family: 'Raleway', sans-serif;
  }
  .stage {
    position: relative; width: 1200px; height: 1200px;
  }
  .card {
    position: absolute; top: 300px;
    width: 420px; height: 600px;
    display: flex; flex-direction: column; align-items: center;
    box-shadow: 0 10px 24px rgba(0,0,0,0.18);
    overflow: hidden;
  }
  .card--front {
    left: 168px;
    background: linear-gradient(90deg, var(--navy-deep) 0%, var(--navy-mid) 60%, var(--navy-light) 100%);
  }
  .card--back {
    left: 617px;
    background: var(--paper);
  }
  .identity {
    position: absolute; top: 235px; left: 0; right: 0;
    display: flex; flex-direction: column; align-items: center;
  }
  .identity__mark { width: 72px; height: 72px; margin-bottom: 14px; }
  .identity__name {
    font-weight: 300; font-size: 22px; letter-spacing: 0.5px;
    text-transform: uppercase; white-space: nowrap;
  }
  .identity__specialty {
    margin-top: 6px;
    font-weight: 400; font-size: 9.5px; letter-spacing: 2.2px;
    text-transform: uppercase;
  }
  .card--front .identity__name { color: var(--ink-light); }
  .card--front .identity__specialty { color: var(--ink-muted); }
  .card--back .identity__name { color: var(--ink-grey); }
  .card--back .identity__specialty { color: var(--ink-sub); }
  .card__band {
    position: absolute; left: 0; right: 0; bottom: 0; height: 16px;
    background: linear-gradient(90deg, var(--band-start), var(--band-end));
  }
</style>
</head>
<body>
<main class="stage">
  <section class="card card--front">
    <div class="identity">
      <svg class="identity__mark" viewBox="0 0 72 72" aria-hidden="true">
        <circle cx="36" cy="36" r="33" fill="none" stroke="#c9d6e2" stroke-width="2"/>
      </svg>
      <p class="identity__name">Marcos Vieira de Andrade</p>
      <p class="identity__specialty">Ortopedia e Traumatologia</p>
    </div>
  </section>

  <section class="card card--back">
    <div class="identity">
      <svg class="identity__mark" viewBox="0 0 72 72" aria-hidden="true">
        <circle cx="36" cy="36" r="33" fill="none" stroke="#9fb6cc" stroke-width="2"/>
      </svg>
      <p class="identity__name">Marcos Vieira de Andrade</p>
      <p class="identity__specialty">Ortopedia e Traumatologia</p>
    </div>
    <div class="card__band"></div>
  </section>
</main>
</body>
</html>
```